Schulungen und Brandschutzdienstleistungen
Zielgruppe
Wir sind im vorbeugenden und organisatorischen Brandschutz tätig. Unsere Zielgruppe sind Firmen die Unterstützung, Beratung und die Schulung Ihrer Mitarbeiter beötigen.
Aufgabenstellung
Vorgaben ergeben sich aus dem Design der Homepage und dem pdf Upload (Beispiel des letzten Flyers).
Es sollen die Schulungsleistungen wie Brandschutzhelfer, Erste Hilfe und Unterweisungen hervorgehoben werden. Weiterhin sollen unsere Dienstleistungen, insbesondere der externe Brandschutzbeauftragte, aufgezeigt werden.
Schön währe auf der letzten Seite ein Anmeldeformular für die Schulungen.
Texte und Logo dürfen gerne verwendet werden.
Die Flyer soll zusammen mit einem Anschreiben in eine DIN lang Briefumschlag passen.

```html
<!DOCTYPE html>
<html lang="de">
<head>
<meta charset="utf-8">
<title>Brandschutz Kolbeck – Flyer 2017</title>
<link href="https://fonts.googleapis.com/css2?family=Source+Sans+3:wght@300;400;600;700&display=swap" rel="stylesheet">
<style>
:root{
  --red:#8f0d0d;
  --red-text:#8a1010;
  --ink:#2b2b2b;
  --band:#ececec;
  --paper:#ffffff;
  --blush:#f6ecec;
  --stage-top:#c6c6c6;
  --stage-bottom:#ebebeb;
}
*{box-sizing:border-box;margin:0;padding:0}
html,body{width:964px;height:1200px;overflow:hidden}
body{
  background:linear-gradient(180deg,var(--stage-top),var(--stage-bottom) 50%,var(--stage-top));
  font-family:"Source Sans 3",sans-serif;color:var(--ink);position:relative;
}
.spread{position:absolute;left:114px;width:719px;height:520px;background:var(--paper);
  box-shadow:4px 5px 6px rgba(0,0,0,.45);overflow:hidden}
.spread--outside{top:35px}
.spread--inside{top:615px;background:var(--blush)}
.abs{position:absolute}
.photo{position:absolute}
.body-text{font-weight:300;font-size:9.2px;line-height:12.2px}
.body-text p{margin-bottom:12.2px}
.justify{text-align:justify}
.red{color:var(--red-text)}
.strong{font-weight:600}

/* outside – panel about */
.about-photo{left:0;top:0;width:239px;height:224px;background:linear-gradient(160deg,#d9dde0,#8a95a3 55%,#2f3440)}
.about-band{left:0;top:224px;width:239px;height:27px;border-top:2px solid var(--red);
  background:linear-gradient(90deg,#f2f2f2,#d8d8d8);border-bottom-right-radius:10px}
.about-band h2{font-size:17px;font-weight:700;color:var(--red);padding:2px 0 0 12px;letter-spacing:.3px}
.about-text{left:5px;top:254px;width:205px}

/* outside – registration */
.form-title{left:252px;top:12px;font-size:18px;font-weight:700;color:var(--red);letter-spacing:.3px}
.field{position:absolute;left:252px;width:213px;display:flex;align-items:flex-end;font-size:9px;font-weight:300}
.field span{white-space:nowrap;margin-right:3px}
.field i{flex:1;border-bottom:1px solid var(--red);height:1px;margin-bottom:2px}
.check{left:252px;top:239px;display:flex;gap:8px;color:var(--red-text);font-size:9.2px;line-height:12px}
.check b{width:11px;height:11px;border:1px solid var(--red);flex:none;margin-top:1px}
.sign-line{position:absolute;top:348px;border-top:1px solid var(--red)}
.sign-label{position:absolute;top:351px;font-size:9px;font-weight:300;text-align:center}
.reach-title{left:243px;width:232px;top:404px;text-align:center;font-size:12.5px;font-weight:600;color:var(--red-text)}
.contact-box{left:243px;top:424px;width:232px;height:96px;background:var(--red);border-radius:10px 10px 0 0;
  color:#fff;font-size:7.2px;line-height:10px;font-weight:300;display:flex;padding:8px 4px 0}
.contact-box div{flex:1;text-align:center}
.contact-box strong{font-weight:600}

/* outside – cover */
.cover-bar-top{left:479px;top:0;width:240px;height:31px;background:var(--red)}
.cover-title{left:479px;top:31px;width:240px;height:82px;padding:6px 0 0 8px;font-size:29px;line-height:35px;font-weight:700;color:var(--red);letter-spacing:.8px}
.cover-bar-mid{left:479px;top:113px;width:240px;height:27px;background:var(--red)}
.cover-photo{left:479px;top:140px;width:240px;height:234px;background:linear-gradient(150deg,#c8ccd2,#6b87b8 55%,#bfc6cf)}
.cover-sub{left:479px;top:374px;width:240px;height:50px;border-top:2px solid var(--red);background:var(--band);
  text-align:right;padding:2px 7px 0 0;font-size:16.5px;line-height:22px;font-weight:700;color:var(--red)}
.cover-year{left:479px;top:424px;width:240px;height:96px;background:var(--red);color:#fff;
  font-size:38px;font-weight:700;text-align:right;padding:22px 20px 0 0}

/* inside */
.swoosh{left:0;top:0}
.tab{position:absolute;top:0;height:43px;background:var(--red);color:#fff;font-size:18px;font-weight:600;padding:15px 0 0 12px}
.tab--left{left:0;width:199px;border-bottom-right-radius:12px}
.tab--right{left:505px;width:214px;border-bottom-left-radius:12px;padding-left:9px;font-size:17.5px}
.helper-intro{left:10px;top:58px;width:222px}
.fire-photo{left:0;top:211px;width:225px;height:129px;border-top-right-radius:12px;background:linear-gradient(120deg,#3d4656,#c7531a 45%,#f7c041 70%,#ececec)}
.fire-caption{left:0;top:340px;width:225px;height:34px;border-top:2px solid var(--red);background:var(--band);
  border-bottom-right-radius:12px;padding:3px 0 0 7px;font-size:9.5px;line-height:12px;font-weight:600;color:var(--red-text)}
.helper-more{left:6px;top:385px;width:226px}
.team-photo{left:239px;top:0;width:240px;height:114px;background:linear-gradient(160deg,#e9eef3,#c9a78f 50%,#dde3ea)}
.course-title{left:239px;top:114px;width:240px;height:69px;border-top:2px solid var(--red);background:var(--band);
  border-bottom-right-radius:12px;text-align:center;font-size:16.5px;line-height:22px;font-weight:700;color:var(--red);padding-top:1px}
.course-text{left:248px;top:195px;width:221px}
.small{font-size:7.5px;line-height:10.2px;font-weight:300}
.small h4{font-weight:600;color:var(--red-text);font-size:7.5px}
.notes{left:248px;top:331px}
.venue{left:248px;top:383px}
.dates-title{left:348px;width:103px;top:384px;text-align:center;font-size:12.5px;font-weight:600;color:var(--red-text)}
.dates{left:348px;top:397px;width:103px;height:123px;background:var(--red);color:#fff;text-align:center;
  font-size:7.5px;line-height:8.6px;padding-top:8px}
.dates p{margin-bottom:8.6px}
.dates span{font-weight:300}
.officer-text{left:487px;top:52px;width:221px}
.detector-photo{left:487px;top:357px;width:232px;height:163px;border-top-left-radius:12px;background:linear-gradient(135deg,#cfd6de,#f4f4f4 45%,#d9dde2)}
</style>
</head>
<body>

<section class="spread spread--outside" aria-label="Flyer Außenseite">
  <div class="photo about-photo" role="img" aria-label="Porträtfoto des Inhabers im Sakko mit Brille"></div>
  <div class="abs about-band"><h2>ÜBER UNS:</h2></div>
  <div class="abs about-text body-text">
    <p>Durch meine knapp 20-jährige Berufserfahrung als aktiver Feuerwehrbeamter wird mir die zerstörerische Kraft eines Feuers und der damit verbundenen Schäden täglich aufs Neue vorgeführt.</p>
    <p>Aufgrund meiner langjährigen Erfahrung im Brandschutz möchte ich mit meinem Unternehmen mit Ihnen gemeinsam die richtigen und vor allem sinnvollen präventiven Brandschutzmaßnahmen ergreifen, um größere Schäden zu verhindern.</p>
    <p>Mein Ziel ist die Aufklärung, Beratung sowie das Training vor Ort und damit der Schutz von Leib, Leben und Sachwerten.</p>
    <p>Mit Ihnen gemeinsam plane ich aus der Praxis für die Praxis.</p>
    <p style="font-weight:400">Markus Kolbeck</p>
  </div>

  <h2 class="abs form-title">ANMELDEFORMULAR:</h2>
  <div class="field" style="top:46px"><span>Name:</span><i></i></div>
  <div class="field" style="top:73px"><span>Vorname:</span><i></i></div>
  <div class="field" style="top:104px"><span>Straße:</span><i></i></div>
  <div class="field" style="top:133px"><span>PLZ, Wohnort:</span><i></i></div>
  <div class="field" style="top:165px"><span>Telefon:</span><i></i></div>
  <div class="field" style="top:193px"><span>E-Mail:</span><i></i></div>
  <div class="abs check"><b></b><span>Ich möchte an der Schulung zum<br>Brandschutzhelfer teilnehmen.</span></div>
  <div class="field" style="top:287px;color:var(--red-text);font-weight:400"><span>Als Termin bevorzuge ich den:</span><i></i></div>
  <div class="sign-line" style="left:252px;width:79px"></div>
  <div class="sign-line" style="left:357px;width:108px"></div>
  <div class="sign-label" style="left:252px;width:79px">Datum</div>
  <div class="sign-label" style="left:357px;width:108px">Unterschrift</div>
  <h3 class="abs reach-title">So erreichen Sie uns:</h3>
  <div class="abs contact-box">
    <div><strong>Brandschutz Kolbeck</strong><br>Ahornstraße 14<br>52249 Eschweiler<br><br>(02403) 555012<br>info@brandschutz-kolbeck.de</div>
    <div>Besuchen Sie uns im Web:<br><br><strong>www.brandschutz-kolbeck.de</strong><br><br>Seminare und Schulungen<br>auch online buchbar.</div>
  </div>

  <div class="abs cover-bar-top"></div>
  <h1 class="abs cover-title">BRANDSCHUTZ<br>KOLBECK</h1>
  <div class="abs cover-bar-mid"></div>
  <div class="photo cover-photo" role="img" aria-label="Zwei Männer begutachten gemeinsam einen Feuerlöscher"></div>
  <div class="abs cover-sub">Schulungen und<br>Dienstleistungen</div>
  <div class="abs cover-year">2017</div>
</section>

<section class="spread spread--inside" aria-label="Flyer Innenseite">
  <svg class="abs swoosh" width="719" height="520" viewBox="0 0 719 520" aria-hidden="true">
    <path d="M0 0H719V150C560 260 380 300 0 290Z" fill="#ffffff"/>
    <path d="M719 260C560 360 360 420 0 420V520H719Z" fill="#fbf5f5"/>
  </svg>

  <h2 class="tab tab--left">Brandschutzhelfer</h2>
  <div class="abs helper-intro body-text justify">
    <p>Nach dem Arbeitsschutzgesetz (§10 ArbSchG – Erste Hilfe und sonstige Notfallmaßnahmen) und den Vorschriften der Berufsgenossenschaften ist jeder Arbeitgeber verpflichtet, in angemessenen Zeitabständen seine Mitarbeiter für das richtige Verhalten im Brandfall zu schulen.</p>
    <p>Seit 01.01.2013 ist die Arbeitsstätten - Regel ASR A2.2 - Maßnahmen gegen Brände, gültig. Darin wird die Zahl der Brandschutzhelfer auf mindestens 5% der Arbeitnehmer festgelegt. Die Versicherer haben dies größtenteils zu Ihren Bedingungen</p>
  </div>
  <div class="photo fire-photo" role="img" aria-label="Person löscht einen Brand mit einem Feuerlöscher"></div>
  <div class="abs fire-caption">Sind Ihre Mitarbeiter ausreichend<br>für den Brand vorbereitet?</div>
  <div class="abs helper-more body-text justify">
    <p>Was nützt Ihnen die Anschaffung gesetzlich vorgeschriebener Feuerlöscher oder Selbsthilfeeinrichtungen, wenn im Ernstfall keiner mit den Geräten umgehen kann. Laut einer Umfrage des bvfs - Bundesverband Feuerschutzbetriebe e.V. haben 69% aller Befragten noch nie an einer Brandschutzschulung aktiv teilgenommen.</p>
    <p>Daher veranstalten wir regelmäßig<br><span class="red" style="font-weight:400">Seminare für Brandschutzhelfer.</span></p>
  </div>

  <div class="photo team-photo" role="img" aria-label="Seminarteilnehmer sitzen lächelnd in einer Reihe"></div>
  <h2 class="abs course-title">Brandschutzhelfer<br>Ausbildung nach DGUV<br>Information 205-023</h2>
  <div class="abs course-text body-text justify">
    <p>Die Ausbildung umfasst ca. drei Unterrichtseinheiten a`45 Minuten. Die Zeitdauer für die Praxis nach Abschnitt 2.2 der DGUV Information 205-023 hängt von der Gruppengröße ab.<br>Jeder Teilnehmer bekommt ausreichend Übungszeit zur Verfügung gestellt.</p>
    <p style="text-align:left">Teilnahmegebühr: 95,00 EURO zzgl. 19%MwSt. Inklusive Tagungsgetränke (Frischer Bohnenkaffee und Tee sowie Softdrinks) und Teilnehmerunterlagen.</p>
  </div>
  <div class="abs notes small"><h4>Hinweise:</h4>Festes Schuhwerk und angepasste Kleidung<br>für Praxisübungen im Freien.<br>Gültiges Ausweisdokument.</div>
  <div class="abs venue small"><h4>Tagungsort:</h4>Tagungshaus Uferblick<br>Am Seeufer 8<br>52249 Eschweiler<br><br>Raum Seeblick</div>
  <h3 class="abs dates-title">Termine 2017</h3>
  <div class="abs dates">
    <p>Mittwoch, 27.04.2016<br><span>von 09:00 - 13:00 Uhr</span></p>
    <p>Mittwoch, 18.05.2016<br><span>von 09:00 - 13:00 Uhr</span></p>
    <p>Mittwoch, 08.06.2016<br><span>von 09:00 - 13:00 Uhr</span></p>
    <p>Mittwoch, 29.06.2016<br><span>von 09:00 - 13:00 Uhr</span></p>
  </div>

  <h2 class="tab tab--right">Brandschutbeauftragter</h2>
  <div class="abs officer-text body-text justify">
    <p>Für den Brandschutz in Betrieben sind aufgrund besonderer Rechtsvorschriften, behördlichen Auflagen oder Gefährdungsbeurteilungen Brandschutzbeauftragte erforderlich, die durch ihre qualifizierte Ausbildung dem Unternehmer/Arbeitgeber als zentraler Partner für brandschutzrelevante Themen zur Verfügung stehen.<br>Je nach Unternehmensgröße ist es effizienter und wirtschaftlicher, diese Aufgabe einem erfahrenen, externen Brandschutzbeauftragten zu übertragen um einen ganzheitlichen Brandschutz im Unternehmen gewährleisten zu können.</p>
    <p class="red" style="font-weight:400;text-align:left">Wir übernehmen für Sie als Unternehmer oder Betreiber einer Immobilie die Funktion des Brandschutzbeauftragten.</p>
    <p>Nutzen Sie die Vorteile von aktuellem Fachwissen und umfangreichen Erfahrungen im vorbeugenden, organisatorischen und abwehrenden Brandschutz.</p>
    <p>Wir würden uns sehr freuen, wenn wir die Aufgabe des externen Brandschutzbeauftragen für Sie übernehmen dürfen.</p>
  </div>
  <div class="photo detector-photo" role="img" aria-label="Rauchmelder vor einem Aushang zum Verhalten im Brandfall"></div>
</section>

</body>
</html>
```